Print & digital package needed for technology firm

We need a package of coordinating marketing materials for our technology business. We offer technology solutions to midsized organizations, including data center, outsourced IT, and technology consulting. Find more information on our website, www.pexlora.com. Design is the main concern, we can modify the text ongoing to best reflect our company’s offerings. The design should communicate technology expertise and strategic thinking. Our website is currently being updated with a “flat design” theme and we’d like design of these items to be flat, fresh, modern, and professional, without being boring.
Please use attached logo - can send in .ai/.eps/.psd/etc. Fonts in logo are Futura, Futura Book, and Lato. Please use pexLORA blue, #0372bb.
Please find attached one of our product flyers for one of the computers we lease. Fonts used are Roboto Slab (partial to this font) & Lato. Also attached copy of our business card design.
Taglines we have used include “Does IT hear what troubles you?” and “IT made simple” although we are open to new ideas.
Would like final products to be available in editable files - .psd/.tif/.ai/etc.

- 1 PowerPoint template
- 1 leaderboard ad (digital, 72dpi)
- 1 medium rectangle ad 300x250 (digital, 72dpi)
- 1 full page ad 8x11 (print, 300dpi)
- 1 half-page ad horizontal (print, 300dpi)
- 1 letterhead template
- 1 proposal front-page

There is potential for further graphic/print design opportunities for our business as well.

All, thank you for your assistance in understanding the budget process with this type of design contest - we have updated the project's budget to reflect the items we are requesting.

Please email mvarga at pexlora.com with inquiries or comments. Thank you.

Designers,

Due to an oversight, our project was listed as "refundable" - this has been corrected and changed to committed payment.
To enter into this contest, please pick 2-3 items from the list of desired materials (ads, powerpoint, letterhead, etc.) It is not necessary to submit all items which will be part of the final package to be considered for the contest.

Thank you. Please contact mvarga@pexlora.com for questions.
Best,
Mimi

CEOs, CFOs, CIOs, COOs - college+ educated, 30-60, professional.

```html
<!DOCTYPE html>
<html lang="en">
<head>
<meta charset="utf-8">
<title>HaaS</title>
<link rel="stylesheet" href="https://fonts.googleapis.com/css2?family=Source+Sans+3:wght@400;600&display=swap">
<style>
  :root {
    --navy-top: #122f55;
    --navy-bottom: #1b5c98;
    --accent-orange: #f9b03f;
    --accent-brown: #9a6128;
    --text-white: #ffffff;
    --button-blue-dark: #1c5d9c;
    --button-blue-light: #3a8fd0;
    --button-grey: #e2e6ea;
    --arrow-navy: #1a3357;
  }
  html, body {
    margin: 0;
    padding: 0;
    overflow: hidden;
    background: #ffffff;
  }
  .banner {
    position: relative;
    width: 1200px;
    height: 457px;
    overflow: hidden;
    background: linear-gradient(180deg, var(--navy-top) 0%, #16467a 55%, var(--navy-bottom) 100%);
    font-family: "Source Sans 3", "Myriad Pro", Arial, sans-serif;
    color: var(--text-white);
  }
  .accent-bar {
    position: absolute;
    left: 0;
    top: 65px;
    width: 22px;
    height: 125px;
    background: var(--accent-orange);
  }
  .headline {
    position: absolute;
    left: 106px;
    top: 63px;
    margin: 0;
    font-size: 155px;
    font-weight: 400;
    line-height: 1;
    letter-spacing: -2px;
    color: var(--accent-orange);
  }
  .rule {
    position: absolute;
    left: 45px;
    top: 209px;
    width: 816px;
    height: 2px;
    background: var(--text-white);
  }
  .intro {
    position: absolute;
    left: 80px;
    top: 234px;
    width: 640px;
    margin: 0;
    font-size: 24px;
    line-height: 29px;
    letter-spacing: 0.3px;
    font-weight: 400;
    white-space: nowrap;
  }
  .cta-button {
    position: absolute;
    left: 83px;
    top: 350px;
    width: 402px;
    height: 60px;
    border-radius: 12px;
    overflow: hidden;
    display: flex;
    text-decoration: none;
    color: var(--text-white);
    box-shadow: 0 3px 6px rgba(0, 0, 0, 0.3);
  }
  .cta-label {
    flex: 1;
    display: flex;
    align-items: center;
    padding-left: 45px;
    font-size: 21px;
    background: linear-gradient(90deg, var(--button-blue-dark) 0%, var(--button-blue-light) 100%);
  }
  .cta-arrow {
    width: 60px;
    display: flex;
    align-items: center;
    justify-content: center;
    background: linear-gradient(180deg, #f4f6f8 0%, var(--button-grey) 100%);
  }
  .device-illustration {
    position: absolute;
    left: 728px;
    top: 62px;
    width: 452px;
    height: 300px;
    border-radius: 18px;
    background: linear-gradient(135deg, rgba(255, 255, 255, 0.22) 0%, rgba(154, 97, 40, 0.35) 55%, rgba(249, 176, 63, 0.4) 100%);
  }
</style>
</head>
<body>
  <div class="banner">
    <div class="accent-bar"></div>
    <h1 class="headline">HaaS</h1>
    <div class="rule"></div>
    <p class="intro">The HaaS flat-fee model not only helps you track expenses,<br>but eliminates large capital outlays and the associated high<br>taxes, because all of our services qualify as operating costs.</p>
    <a class="cta-button" href="#">
      <span class="cta-label">Learn more about HaaS</span>
      <span class="cta-arrow">
        <svg width="14" height="22" viewBox="0 0 14 22" aria-hidden="true">
          <polygon points="0,0 14,11 0,22" fill="var(--arrow-navy)"/>
        </svg>
      </span>
    </a>
    <div class="device-illustration" role="img" aria-label="Flat icon group of hardware: a speaker, a computer mouse, a wireless signal symbol and an orange device tile"></div>
  </div>
</body>
</html>
```